Book cover for a New Adult, romance/ contemporary novel.

I need a full front, back, and spine cover for my upcoming book. The novel is a romance/ coming of age book and is similar to Every Quiet Harbor by Marissa Colfax. My main audience is women in their late teens/ early 20's. The book is an emotional, reminiscent piece and I would love to see some cover designs with a darker palette like Waiting on Belmora, Nine Rooms Between, or Bartholomew and Kip (but I also adore some lighter covers, especially those that feature the couple such as A Different Then or Past Each Hour). Feel free to send some minimal designs as well if you have any! A great idea of that would be the cover for Salt and Clover or Waiting on Belmora. If you go with a minimal design, I'd love to see silhouettes or maybe a burning candle. Another possible idea I thought of would be a scene at a concert with the crowd silhouetted and then my main character (more details on her below) standing in the middle of it all. I prefer animation/drawing etc over real models. But feel free to send me whatever you think might match the vibe, I'd love to see anything you have in mind! Some main symbols in my book are stars and candles. The main character (Marisol) is a female Korean with brown, medium length straight hair, and the love interest (Theo) is a tall and thin male Caucasian with curly brown hair. The book is openly emotional, wistful, and sets an ache in your chest, so I can't wait to see what designs you artists come up with! (My barcode will need to be included on the back cover, and I am getting that soon!)
The title is "The Weight of Daylight" and the author's name is Brenna Quill. The book's dimensions will be 5.5x8.25. The blurb for the back cover is:
When happily ever falls apart, all you can do is move forward… and reminisce. Marisol Ahn returns home from college following a tragic incident she can’t bring herself to talk about and a breakup with her boyfriend, Theo Marsh. Finding it difficult to confront her traumas, she begins therapy. Marisol takes the therapist on a rollercoaster journey of her college life, retelling the events that caused her relationship to spiral out of control and led to her dropping out of pre-med despite that being her life-long dream. Marisol sets out to remember how things were before everything got so messed up, and figure out how to continue living now that they are.
The author bio for the back cover is:
Brenna Quill is the author of The Restless and Bold. She is a self published writer from Las Vegas who likes to pretend she’s currently in a New York bookstore, drinking a latte, while listening to a carefully curated playlist. When she’s not writing, Brenna is taking care of her plant babies and cuddling with the cutest puppy in the world.

```html
<!DOCTYPE html>
<html lang="en">
<head>
<meta charset="utf-8">
<title>The Weight of Daylight – Cover</title>
<link rel="stylesheet" href="https://fonts.googleapis.com/css2?family=Amatic+SC:wght@400;700&family=Montserrat:wght@400;500&display=swap">
<style>
  :root {
    --sky-top: #5f9fc0;
    --sky-mid: #8cc8d6;
    --sky-bottom: #bdf2e6;
    --paper: #fbfbef;
    --plum: #8b1f66;
    --ink-blue: #2a22aa;
    --deep-navy: #1f1594;
    --tile-cyan: #63d2e4;
    --white: #ffffff;
    --title-font: "Amatic SC", "Comic Neue", cursive;
    --body-font: "Montserrat", "Helvetica Neue", Arial, sans-serif;
  }
  html, body {
    margin: 0;
    padding: 0;
    width: 1200px;
    height: 2400px;
    overflow: hidden;
    background: var(--white);
  }
  .canvas {
    position: relative;
    width: 1200px;
    height: 2400px;
  }
  .front-cover {
    position: absolute;
    left: 219px;
    top: 56px;
    width: 769px;
    height: 1116px;
    box-shadow: 14px 16px 18px rgba(0,0,0,0.45);
  }
  .full-wrap {
    position: absolute;
    left: 66px;
    top: 1420px;
    width: 1076px;
    height: 718px;
    background: linear-gradient(180deg, var(--sky-top) 0%, var(--sky-mid) 50%, var(--sky-bottom) 100%);
    box-shadow: 14px 16px 18px rgba(0,0,0,0.45);
  }
  .full-wrap svg { position: absolute; }
  .back-stars { left: 0; top: 0; }
  .spine-art { left: 0; top: 0; }
  .wrap-front { left: 582px; top: 0; }
  .back-title, .back-author {
    position: absolute;
    left: 52px;
    margin: 0;
    font-family: var(--title-font);
    font-weight: 700;
    font-size: 60px;
    line-height: 1;
    letter-spacing: 1px;
  }
  .back-title { top: 44px; color: var(--white); }
  .back-author { top: 400px; color: var(--ink-blue); }
  .back-copy {
    position: absolute;
    left: 52px;
    width: 392px;
    margin: 0;
    font-family: var(--body-font);
    font-size: 12px;
    line-height: 14.5px;
    text-align: justify;
  }
  .back-blurb { top: 124px; color: var(--white); }
  .back-bio { top: 472px; color: var(--deep-navy); }
  .title-word { font-family: var(--title-font); font-weight: 700; fill: var(--plum); }
  .name-word { font-family: var(--title-font); font-weight: 700; }
  .frame { fill: var(--paper); }
  .star { fill: #dff4f8; }
</style>
</head>
<body>
<div class="canvas">

  <!-- Front cover -->
  <svg class="front-cover" viewBox="0 0 820 1190" xmlns="http://www.w3.org/2000/svg">
    <defs>
      <linearGradient id="sky" x1="0" y1="0" x2="0" y2="1">
        <stop offset="0" stop-color="#5f9fc0"/>
        <stop offset="0.5" stop-color="#8cc8d6"/>
        <stop offset="1" stop-color="#bdf2e6"/>
      </linearGradient>
      <linearGradient id="photo-warm" x1="0" y1="0" x2="1" y2="1">
        <stop offset="0" stop-color="#9cc6d2"/>
        <stop offset="0.55" stop-color="#b4743e"/>
        <stop offset="1" stop-color="#d9a982"/>
      </linearGradient>
      <linearGradient id="photo-portrait" x1="0" y1="0" x2="0" y2="1">
        <stop offset="0" stop-color="#5a3b2c"/>
        <stop offset="0.5" stop-color="#d8a68a"/>
        <stop offset="1" stop-color="#34386e"/>
      </linearGradient>
      <linearGradient id="photo-sleeve" x1="0" y1="0" x2="0" y2="1">
        <stop offset="0" stop-color="#b97a3c"/>
        <stop offset="0.3" stop-color="#d7e8ef"/>
        <stop offset="1" stop-color="#aecfe0"/>
      </linearGradient>
      <linearGradient id="photo-arm" x1="0" y1="0" x2="1" y2="1">
        <stop offset="0" stop-color="#dfeef4"/>
        <stop offset="1" stop-color="#a9cad9"/>
      </linearGradient>
      <linearGradient id="photo-gingham" x1="0" y1="0" x2="1" y2="1">
        <stop offset="0" stop-color="#3a4580"/>
        <stop offset="0.6" stop-color="#6f7fae"/>
        <stop offset="1" stop-color="#c9dde7"/>
      </linearGradient>
      <radialGradient id="photo-candle" cx="0.6" cy="0.25" r="0.9">
        <stop offset="0" stop-color="#ffffff"/>
        <stop offset="0.35" stop-color="#bff0f6"/>
        <stop offset="1" stop-color="#5fcadf"/>
      </radialGradient>
      <filter id="tile-shadow" x="-20%" y="-20%" width="140%" height="140%">
        <feDropShadow dx="4" dy="6" stdDeviation="5" flood-color="#1d4a5c" flood-opacity="0.35"/>
      </filter>
      <path id="star-shape" d="M0,-10 L2.9,-4 9.5,-3.1 4.7,1.5 5.9,8.1 0,5 -5.9,8.1 -4.7,1.5 -9.5,-3.1 -2.9,-4Z"/>

      <symbol id="star-field" viewBox="0 0 820 1190">
        <g class="star" opacity="0.55">
          <use href="#star-shape" transform="translate(40 25) scale(1.2)"/>
          <use href="#star-shape" transform="translate(130 90) scale(0.8)"/>
          <use href="#star-shape" transform="translate(210 30) scale(0.7)"/>
          <use href="#star-shape" transform="translate(85 165) scale(1.6)"/>
          <use href="#star-shape" transform="translate(190 150) scale(1.1)"/>
          <use href="#star-shape" transform="translate(260 100) scale(0.6)"/>
          <use href="#star-shape" transform="translate(330 45) scale(0.9)"/>
          <use href="#star-shape" transform="translate(420 120) scale(0.7)"/>
          <use href="#star-shape" transform="translate(470 40) scale(1.3)"/>
          <use href="#star-shape" transform="translate(520 100) scale(0.8)"/>
          <use href="#star-shape" transform="translate(600 60) scale(1.1)"/>
          <use href="#star-shape" transform="translate(680 20) scale(0.7)"/>
          <use href="#star-shape" transform="translate(700 115) scale(1.4)"/>
          <use href="#star-shape" transform="translate(780 80) scale(1.0)"/>
          <use href="#star-shape" transform="translate(560 150) scale(1.5)"/>
          <use href="#star-shape" transform="translate(760 200) scale(0.8)"/>
          <use href="#star-shape" transform="translate(30 300) scale(0.7)"/>
          <use href="#star-shape" transform="translate(795 330) scale(0.6)"/>
          <use href="#star-shape" transform="translate(20 620) scale(0.9)"/>
          <use href="#star-shape" transform="translate(40 760) scale(0.6)"/>
          <use href="#star-shape" transform="translate(790 560) scale(0.7)"/>
          <use href="#star-shape" transform="translate(800 850) scale(0.5)"/>
        </g>
        <g fill="#eafaff" opacity="0.6">
          <circle cx="60" cy="60" r="1.6"/><circle cx="110" cy="40" r="1.2"/><circle cx="170" cy="70" r="1.5"/>
          <circle cx="240" cy="60" r="1.1"/><circle cx="300" cy="130" r="1.4"/><circle cx="360" cy="90" r="1.2"/>
          <circle cx="390" cy="30" r="1.5"/><circle cx="440" cy="80" r="1.1"/><circle cx="500" cy="140" r="1.3"/>
          <circle cx="560" cy="30" r="1.2"/><circle cx="640" cy="110" r="1.5"/><circle cx="730" cy="50" r="1.2"/>
          <circle cx="800" cy="140" r="1.4"/><circle cx="20" cy="210" r="1.3"/><circle cx="50" cy="420" r="1.2"/>
          <circle cx="30" cy="520" r="1.4"/><circle cx="800" cy="440" r="1.3"/><circle cx="790" cy="700" r="1.1"/>
          <circle cx="25" cy="900" r="1.2"/><circle cx="120" cy="1120" r="1.1"/><circle cx="400" cy="1150" r="1.2"/>
          <circle cx="700" cy="1100" r="1.1"/><circle cx="280" cy="190" r="1.2"/><circle cx="650" cy="180" r="1.3"/>
        </g>
      </symbol>

      <symbol id="cover-art" viewBox="0 0 820 1190">
        <use href="#star-field" x="0" y="0" width="820" height="1190"/>
        <g filter="url(#tile-shadow)">
          <!-- row 1 -->
          <g transform="translate(156 282) rotate(-8)" role="img" aria-label="Photograph fragment: young woman's hair beside a window">
            <rect class="frame" x="-120" y="-108" width="240" height="216"/>
            <rect x="-108" y="-96" width="216" height="192" fill="url(#photo-warm)"/>
          </g>
          <g transform="translate(386 272) rotate(-2)" role="img" aria-label="Photograph fragment: young woman resting her head on her arms">
            <rect class="frame" x="-116" y="-112" width="232" height="224"/>
            <rect x="-104" y="-100" width="208" height="200" fill="url(#photo-portrait)"/>
          </g>
          <g transform="translate(626 250) rotate(-12)" role="img" aria-label="Photograph fragment: shoulder in a white sweater">
            <rect class="frame" x="-116" y="-110" width="232" height="220"/>
            <rect x="-104" y="-98" width="208" height="196" fill="url(#photo-sleeve)"/>
          </g>

          <!-- row 2 -->
          <g transform="translate(176 515) rotate(-3)">
            <rect class="frame" x="-115" y="-120" width="230" height="240"/>
            <text class="title-word" x="-95" y="-30" font-size="62">THE</text>
            <text class="title-word" x="-97" y="45" font-size="106" textLength="196" lengthAdjust="spacingAndGlyphs">WEIGHT</text>
            <text class="title-word" x="-95" y="94" font-size="50">OF</text>
          </g>
          <g transform="translate(411 500) rotate(-4)">
            <rect class="frame" x="-115" y="-118" width="230" height="236"/>
            <text class="title-word" font-size="88" transform="translate(-92 82) rotate(-36)" textLength="232" lengthAdjust="spacingAndGlyphs">DAYLIGHT</text>
          </g>
          <g transform="translate(641 482) rotate(-2)" role="img" aria-label="Photograph fragment: arm in a white sweater">
            <rect class="frame" x="-112" y="-116" width="224" height="232"/>
            <rect x="-100" y="-104" width="200" height="208" fill="url(#photo-arm)"/>
          </g>

          <!-- row 3 -->
          <g transform="translate(196 752) rotate(-12)" role="img" aria-label="Photograph fragment: gingham skirt and knee">
            <rect class="frame" x="-120" y="-110" width="240" height="220"/>
            <rect x="-108" y="-98" width="216" height="196" fill="url(#photo-gingham)"/>
          </g>
          <g transform="translate(431 732) rotate(2)" role="img" aria-label="Photograph fragment: sleeve cuff over gingham fabric">
            <rect class="frame" x="-113" y="-114" width="226" height="228"/>
            <rect x="-101" y="-102" width="202" height="204" fill="url(#photo-gingham)"/>
          </g>
          <g transform="translate(671 717) rotate(-12)" role="img" aria-label="Photograph fragment: elbow over gingham fabric">
            <rect class="frame" x="-115" y="-115" width="230" height="230"/>
            <rect x="-103" y="-103" width="206" height="206" fill="url(#photo-gingham)"/>
          </g>

          <!-- row 4 -->
          <g transform="translate(181 930) rotate(4)">
            <rect class="frame" x="-113" y="-118" width="226" height="236"/>
            <rect x="-101" y="-106" width="202" height="212" fill="var(--tile-cyan)"/>
            <text class="name-word" x="0" y="22" font-size="84" fill="var(--ink-blue)" text-anchor="middle" textLength="168" lengthAdjust="spacingAndGlyphs">BRENNA</text>
          </g>
          <g transform="translate(411 945)">
            <rect class="frame" x="-116" y="-116" width="232" height="232"/>
            <rect x="-104" y="-104" width="208" height="208" fill="var(--deep-navy)"/>
            <text class="name-word" x="0" y="26" font-size="92" fill="var(--white)" text-anchor="middle" textLength="150" lengthAdjust="spacingAndGlyphs">QUILL</text>
          </g>
          <g transform="translate(646 955) rotate(3)" role="img" aria-label="Photograph: a pale blue burning candle glowing against soft light">
            <rect class="frame" x="-113" y="-118" width="226" height="236"/>
            <rect x="-101" y="-106" width="202" height="212" fill="url(#photo-candle)"/>
          </g>
        </g>
      </symbol>
    </defs>
    <rect width="820" height="1190" fill="url(#sky)"/>
    <use href="#cover-art" x="0" y="0" width="820" height="1190"/>
  </svg>

  <!-- Full wrap: back, spine, front -->
  <div class="full-wrap">
    <svg class="back-stars" width="582" height="718" viewBox="0 0 820 1190" preserveAspectRatio="none" xmlns="http://www.w3.org/2000/svg" aria-hidden="true">
      <use href="#star-field" x="0" y="0" width="820" height="1190"/>
    </svg>

    <h2 class="back-title">THE WEIGHT OF DAYLIGHT</h2>
    <p class="back-copy back-blurb">When happily ever falls apart, all you can do is move forward… and reminisce. Marisol Ahn returns home from college following a tragic incident she can’t bring herself to talk about and a breakup with her boyfriend, Theo Marsh. Finding it difficult to confront her traumas, she begins therapy. Marisol takes the therapist on a rollercoaster journey of her college life, retelling the events that caused her relationship to spiral out of control and led to her dropping out of pre-med despite that being her life-long dream. Marisol sets out to remember how things were before everything got so messed up, and figure out how to continue living now that they are.</p>
    <h3 class="back-author">BRENNA QUILL</h3>
    <p class="back-copy back-bio">Brenna Quill is the author of The Restless and Bold. She is a self published writer from Las Vegas who likes to pretend she’s currently in a New York bookstore, drinking a latte, while listening to a carefully curated playlist. When she’s not writing, Brenna is taking care of her plant babies and cuddling with the cutest puppy in the world.</p>

    <svg class="spine-art" width="1076" height="718" viewBox="0 0 1076 718" xmlns="http://www.w3.org/2000/svg">
      <text class="title-word" transform="translate(518 50) rotate(90)" font-size="62">
        <tspan font-size="46">THE </tspan><tspan>WEIGHT </tspan><tspan font-size="40">OF </tspan><tspan>DAYLIGHT</tspan><tspan fill="#ffffff" font-size="40"> ★ </tspan><tspan font-size="50">BRENNA QUILL</tspan>
      </text>
    </svg>

    <svg class="wrap-front" width="492" height="714" viewBox="0 0 820 1190" xmlns="http://www.w3.org/2000/svg">
      <use href="#cover-art" x="0" y="0" width="820" height="1190"/>
    </svg>
  </div>

</div>
</body>
</html>
```